Hello - our company Tarvish Health develops novel dietary supplements. We're looking for a label design for a new product. The product is a premium MALE ENHANCEMENT supplement. Below is a link to other competitive products on Bazelo. We’re looking for a powerful, dynamic design. The bottle will be a white 150cc supplement bottle.

The product name is Zantomax

https://www.bazelo-market.com/s?k=male+enhancement&crid=QTMPWD48XN2B&sprefix=male+enhancement%2Caps%2C52&ref=nb_sb_noss_2

Label size in inches - Rectangle 5.5"w x 2.5"h

```html
<!DOCTYPE html>
<html lang="en">
<head>
<meta charset="utf-8">
<title>Zantomax Label</title>
<link href="https://fonts.googleapis.com/css2?family=Arimo:wght@400;700&family=Exo+2:ital,wght@1,700;1,800&family=Michroma&display=swap" rel="stylesheet">
<style>
  :root {
    --page: #ffffff;
    --label: #2c2c2e;
    --text: #c9c9c9;
    --text-bright: #dcdcdc;
    --rule: #b4b4b4;
    --band: #a9a9a9;
    --band-text: #3a3a3a;
    --badge: #1f1f21;
  }
  * { box-sizing: border-box; margin: 0; padding: 0; }
  html, body { width: 1200px; height: 675px; overflow: hidden; background: var(--page); }
  body { position: relative; font-family: "Arimo", Arial, sans-serif; color: var(--text); }

  .label {
    position: absolute; left: 50px; top: 87px;
    width: 1100px; height: 500px;
    background: var(--label);
    overflow: hidden;
  }

  .info { position: absolute; left: 59px; top: 32px; width: 315px; font-size: 12px; line-height: 15.5px; }
  .info p { margin-bottom: 12px; }
  .info strong { color: var(--text-bright); }
  .info .intro { margin-bottom: 17px; }
  .info .warning { margin-bottom: 27px; }

  .disclaimer {
    position: absolute; left: 59px; top: 255px; width: 312px; height: 60px;
    border: 2px solid var(--rule); font-size: 11px; line-height: 14px;
    text-align: center; padding: 6px 8px 0;
  }
  .barcode-slot {
    position: absolute; left: 57px; top: 334px; width: 158px; height: 70px;
    border: 2px solid var(--rule); font-size: 13.5px; color: var(--text-bright);
    display: flex; align-items: center; justify-content: center;
  }
  .maker {
    position: absolute; left: 222px; top: 336px; width: 160px;
    font-size: 11.3px; line-height: 14px; font-weight: 700; color: var(--text-bright);
  }

  .brand-column { position: absolute; left: 0; top: 0; width: 1100px; height: 500px; }

  .facts {
    position: absolute; left: 751px; top: 35px; width: 279px; height: 341px;
    border: 3px solid var(--rule); border-radius: 10px; overflow: hidden;
    font-size: 10.5px;
  }
  .facts-title {
    background: var(--rule); color: var(--label);
    font-size: 22px; font-weight: 700; text-align: center;
    height: 28px; line-height: 30px; letter-spacing: .2px;
  }
  .facts-serving {
    display: flex; justify-content: space-between;
    padding: 7px 6px 0 7px; height: 28px; border-bottom: 5px solid var(--rule);
  }
  .facts-head {
    display: flex; justify-content: flex-end; gap: 8px;
    font-size: 9.5px; font-weight: 700; color: var(--text-bright);
    padding: 4px 12px 3px; border-bottom: 3px solid var(--rule);
  }
  .facts-row {
    display: grid; grid-template-columns: 1fr 50px 28px;
    padding: 3px 6px 2px 7px; border-bottom: 3px solid var(--rule);
    line-height: 12px;
  }
  .facts-row .amount { text-align: right; }
  .facts-row .dv { text-align: center; }
  .facts-row small { display: block; font-size: 8px; line-height: 10px; padding-left: 12px; }
  .facts-row.last { border-bottom-width: 6px; }
  .facts-note { padding: 6px 7px; font-size: 10px; }

  .other-ingredients {
    position: absolute; left: 751px; top: 387px; width: 290px;
    font-size: 12.5px; line-height: 16px;
  }
  .badges { position: absolute; left: 783px; top: 422px; width: 220px; height: 50px; }

  .bottom-band {
    position: absolute; left: 0; bottom: 0; width: 1100px; height: 37px;
    background: var(--band);
    display: flex; align-items: center; justify-content: center;
    font-family: "Exo 2", sans-serif; font-style: italic; font-weight: 800;
    font-size: 13px; letter-spacing: 2px; color: var(--band-text);
  }
  .bottom-band .count { width: 170px; text-align: right; padding-right: 20px; }
  .bottom-band .divider { width: 2px; height: 26px; background: var(--band-text); }
  .bottom-band .kind { width: 270px; padding-left: 20px; }
</style>
</head>
<body>
<main class="label">

  <section class="info">
    <p class="intro">Your Company Description/Goals (Optional)</p>
    <p><strong>Suggested Use:</strong> Take 2 Gummies per day. Do not exceed suggested dosage.</p>
    <p class="warning"><strong>WARNING:</strong> Intended for use by adults 18 years of age and over. Do not use if the seal is broken. If you are pregnant, nursing, taking any medications or have any medical condition, consult your doctor before use.</p>
    <p><strong>Storage:</strong> Store in a cool, dry place away from heat and moisture.</p>
  </section>

  <div class="disclaimer">*These statements have not been evaluated by the Food and Drug Administration. This product is not intended to diagnose, treat, cure, or prevent any disease.</div>
  <div class="barcode-slot">YOUR BARCODE</div>
  <div class="maker">Manufactured for:<br>Your Company Name<br>Company Street Address<br>City,State,Zip<br>Phone Number<br>(Optional),Website<br>(Optional), Email (Optional)</div>

  <svg class="brand-column" viewBox="0 0 1100 500" aria-label="Zantomax extra strength male enhancement supplement 1200mg">
    <g fill="#c9c9c9">
      <text transform="translate(477,248) rotate(-90)" font-family="Michroma, sans-serif" font-size="14" textLength="192" lengthAdjust="spacingAndGlyphs">EXTRA STRENGTH</text>
      <text transform="translate(559,450) rotate(-90)" font-family="Michroma, sans-serif" font-size="76" textLength="434" lengthAdjust="spacingAndGlyphs">ZANTOMAX</text>
      <text transform="translate(603,333) rotate(-90)" font-family="'Exo 2', sans-serif" font-style="italic" font-weight="800" font-size="19" letter-spacing="2" textLength="276" lengthAdjust="spacingAndGlyphs">MALE ENHANCEMENT</text>
      <text transform="translate(624,232) rotate(-90)" font-family="'Exo 2', sans-serif" font-style="italic" font-weight="800" font-size="19" letter-spacing="2" textLength="175" lengthAdjust="spacingAndGlyphs">SUPPLEMENT</text>
    </g>
    <g stroke="#c9c9c9" stroke-width="2">
      <line x1="483" y1="58" x2="483" y2="427"/>
      <line x1="571" y1="58" x2="571" y2="427"/>
    </g>
    <polygon points="629,72 652,58 652,170 629,170" fill="#b9b9b9"/>
    <text transform="translate(648,164) rotate(-90)" font-family="'Exo 2', sans-serif" font-style="italic" font-weight="800" font-size="20" fill="#2c2c2e" textLength="94" lengthAdjust="spacingAndGlyphs">1200MG</text>
    <g font-family="'Exo 2', sans-serif" font-style="italic" font-weight="800" font-size="12" fill="#d6d6d6" letter-spacing="1">
      <text x="596" y="374">VIRILITY</text>
      <text x="596" y="397">VITALITY</text>
      <text x="596" y="421">VIGOR</text>
    </g>
    <g stroke="#c9c9c9" stroke-width="1.5">
      <line x1="590" y1="378" x2="666" y2="378"/>
      <line x1="590" y1="401" x2="666" y2="401"/>
      <line x1="590" y1="425" x2="666" y2="425"/>
    </g>
    <g fill="#c9c9c9">
      <rect x="587" y="380" width="5" height="5"/>
      <rect x="587" y="403" width="5" height="5"/>
      <rect x="587" y="427" width="5" height="5"/>
    </g>
  </svg>

  <section class="facts">
    <div class="facts-title">SUPPLEMENT FACTS</div>
    <div class="facts-serving"><span>Serving Size : 2 Capsules</span><span>Serving Per Container : 30</span></div>
    <div class="facts-head"><span>Amount Per Serving</span><span>%Daily Value</span></div>
    <div class="facts-row"><span>Horny Goat Weed Extract<small>(Epimedium sagittatum) aerial plant)</small><small>(providing 10mg of icariins)</small></span><span class="amount">1000 mg</span><span class="dv">*</span></div>
    <div class="facts-row"><span>Maca Root Powder</span><span class="amount">250 mg</span><span class="dv">*</span></div>
    <div class="facts-row"><span>Tribulus terrestris 40% Extract<small>(aerial parts)</small></span><span class="amount">60 mg</span><span class="dv">*</span></div>
    <div class="facts-row"><span>Polypodium vulgare Powder<small>(root &amp; rhizome)</small></span><span class="amount">20 mg</span><span class="dv">*</span></div>
    <div class="facts-row"><span>Tongkat Ali Root Powder<small>(Eurycoma longifolia)</small></span><span class="amount">100 mg</span><span class="dv">*</span></div>
    <div class="facts-row"><span>Saw Palmetto Berry Powder</span><span class="amount">100 mg</span><span class="dv">*</span></div>
    <div class="facts-row"><span>Muria Puama Root Powder</span><span class="amount">20 mg</span><span class="dv">*</span></div>
    <div class="facts-row"><span>L-Arginine ( L-Arginine HCl)</span><span class="amount">20 mg</span><span class="dv">*</span></div>
    <div class="facts-row last"><span>Panax ginseng root powder</span><span class="amount">100 mg</span><span class="dv">*</span></div>
    <div class="facts-note">* Daily Value not established</div>
  </section>

  <p class="other-ingredients">Other Ingredients : Rice flour, Gelatin (bovine), and vegetable magnesium stearate</p>

  <svg class="badges" viewBox="0 0 220 50" role="img" aria-label="Certification badges">
    <g fill="var(--badge)" stroke="#b4b4b4" stroke-width="2">
      <circle cx="24" cy="25" r="22"/>
      <circle cx="79" cy="25" r="22"/>
      <circle cx="135" cy="25" r="22"/>
      <circle cx="190" cy="25" r="22"/>
    </g>
  </svg>

  <footer class="bottom-band">
    <span class="count">60 CAPSULES</span>
    <span class="divider"></span>
    <span class="kind">DIETARY SUPPLEMENT</span>
  </footer>
</main>
</body>
</html>
```